Elegant wordpress web page for wedding rental of hand sanitizers

We want to rent our hand sanitizing towers out for high-end weddings. We need a very elegant, sophisticated page that describes our offering. You can see an ugly first draft here: purvant.com/weddings
Target Market(s)
Wedding planners, wedding parents
Number of Pages Required
1 page
Font styles to use
Serif
Script
Colors
Designer to choose colors to be used in the design.
Requirements
Nice to have
- Two wedding-related sites for inspiration: lacetrellisweddings-dot-com and fennoreventservices-dot-com

```html
<!DOCTYPE html>
<html lang="en">
<head>
<meta charset="utf-8">
<title>Purvant Products – Wedding Sanitizer Towers</title>
<link href="https://fonts.googleapis.com/css2?family=Montserrat:wght@500;600;700;800&family=Open+Sans:wght@400;600&display=swap" rel="stylesheet">
<style>
:root{
  --blue:#1b9bd7;
  --teal:#3cc3c6;
  --ink:#222a30;
  --body:#3b4248;
  --white:#ffffff;
  --foot:#eeeeef;
  --photo-green:#7d8a6a;
  --photo-warm:#d9c7b8;
}
*{margin:0;padding:0;box-sizing:border-box}
html,body{width:1200px;height:4736px;overflow:hidden}
body{position:relative;background:var(--white);font-family:"Open Sans",sans-serif;color:var(--body)}
.abs{position:absolute}
.site-header{left:0;top:0;width:1200px;height:120px;background:var(--white);z-index:5}
.brand{left:150px;top:30px;font-family:"Montserrat",sans-serif;font-weight:700;font-size:44px;color:var(--blue);letter-spacing:-1px}
.nav{right:150px;top:52px;display:flex;gap:40px;font-family:"Montserrat",sans-serif;font-weight:600;font-size:19px;color:var(--ink)}
.nav a{color:inherit;text-decoration:none;padding-bottom:6px}
.nav a.active{color:var(--blue);border-bottom:3px solid var(--blue)}
.hero{left:0;top:120px;width:1200px;height:700px}
.hero-title{left:520px;top:330px;font-family:"Montserrat",sans-serif;font-weight:700;font-size:48px;line-height:56px;color:var(--white);text-transform:uppercase}
.heading{font-family:"Montserrat",sans-serif;font-weight:800;font-size:34px;line-height:42px;color:var(--ink);text-transform:uppercase}
.heading em{font-style:normal;color:var(--blue)}
.on-blue .heading{color:var(--white)}
.lead{font-size:17px;font-weight:600;line-height:24px;margin-top:22px;color:var(--body)}
.points{list-style:none;margin-top:22px}
.points li{position:relative;padding-left:36px;font-size:18px;line-height:26px;margin-bottom:18px}
.points li svg{position:absolute;left:0;top:2px}
.on-blue .points li{color:var(--white);font-size:21px;line-height:30px}
.btn{display:inline-block;margin-top:14px;padding:14px 36px;border-radius:30px;background:var(--blue);color:var(--white);font-family:"Montserrat",sans-serif;font-weight:700;font-size:15px;text-transform:uppercase;letter-spacing:.3px}
.on-blue .btn{background:transparent;border:3px solid var(--white)}
.photo{overflow:hidden}
.footer-text{left:0;width:1200px;text-align:center;font-size:15px;color:var(--body);letter-spacing:.3px}
.social{left:530px;top:4546px;display:flex;gap:16px}
.social span{width:30px;height:30px;background:var(--blue);border-radius:4px}
.foot-brand{left:0;width:1200px;top:4650px;text-align:center;font-family:"Montserrat",sans-serif;font-weight:700;font-size:42px;color:var(--blue)}
</style>
</head>
<body>
<svg width="0" height="0" class="abs"><defs>
  <linearGradient id="band" x1="0" y1="0" x2="1" y2="1"><stop offset="0" stop-color="#1b9bd7"/><stop offset="1" stop-color="#3cc3c6"/></linearGradient>
  <linearGradient id="garden" x1="0" y1="0" x2="1" y2="1"><stop offset="0" stop-color="#8f9c78"/><stop offset=".55" stop-color="#d6c8bb"/><stop offset="1" stop-color="#e9d5d0"/></linearGradient>
  <symbol id="drop" viewBox="0 0 20 26"><path d="M10 1C7 7 2 12 2 17a8 8 0 0 0 16 0C18 12 13 7 10 1z" fill="none" stroke="currentColor" stroke-width="2.4"/></symbol>
</defs></svg>

<header class="abs site-header">
  <div class="abs brand">purvant</div>
  <nav class="abs nav"><a href="#">About</a><a class="active" href="#">Products</a><a href="#">Industry Solutions</a><a href="#">Contact</a>
    <svg width="22" height="22" viewBox="0 0 22 22"><circle cx="9" cy="9" r="7" fill="none" stroke="#1b9bd7" stroke-width="3"/><path d="M14 14l6 6" stroke="#1b9bd7" stroke-width="3"/></svg></nav>
</header>

<!-- hero -->
<svg class="abs hero" viewBox="0 0 1200 700" role="img" aria-label="Wedding couple beside a customized sanitizer tower with a floral centerpiece">
  <rect width="1200" height="700" fill="url(#garden)"/>
  <path d="M0 640 C300 700 700 560 1200 600 L1200 700 L0 700Z" fill="#fff"/>
  <path d="M0 640 C300 700 700 560 1200 600" fill="none" stroke="#1b9bd7" stroke-width="8"/>
</svg>
<h1 class="abs hero-title">Welcome to<br>Purvant Products</h1>

<!-- section 1 -->
<section class="abs" style="left:152px;top:860px;width:470px">
  <h2 class="heading">Welcome your <em>guests with something truly unique</em> – a customized hand sanitizer</h2>
  <p class="lead">Why have a generic, industrial hand sanitizer when you could have something truly unique and different?</p>
  <ul class="points">
    <li><svg width="20" height="26" style="color:var(--blue)"><use href="#drop"/></svg>Customize the photo above the spout and the spout decoration</li>
    <li><svg width="20" height="26" style="color:var(--blue)"><use href="#drop"/></svg>Choose any size and shape photo you wish</li>
    <li><svg width="20" height="26" style="color:var(--blue)"><use href="#drop"/></svg>Choose from our standard spout decorations or design one of your own. We'll take care of producing and fitting it</li>
  </ul>
  <span class="btn">Check price and availability</span>
</section>
<svg class="abs" style="left:630px;top:830px" width="350" height="350" viewBox="0 0 350 350" role="img" aria-label="Custom photo sanitizer tower at a wedding reception">
  <circle cx="175" cy="175" r="168" fill="#b99a8a"/><circle cx="175" cy="175" r="168" fill="none" stroke="#1b9bd7" stroke-width="6"/>
</svg>

<!-- section 2 -->
<svg class="abs" style="left:0;top:1390px" width="1200" height="800" viewBox="0 0 1200 800">
  <path d="M0 20 C400 -10 800 90 1200 40 L1200 760 C800 820 400 700 0 760Z" fill="url(#band)"/>
  <path d="M0 20 C250 0 400 40 560 60 L560 770 C350 740 150 740 0 760Z" fill="url(#garden)" role="img" aria-label="Bride and groom beside their photo sanitizer tower"/>
</svg>
<section class="abs on-blue" style="left:628px;top:1560px;width:470px">
  <h2 class="heading">Customize your sanitizer with any photo, any size, any shape</h2>
  <ul class="points" style="margin-top:30px">
    <li><svg width="20" height="26" style="color:#fff"><use href="#drop"/></svg>Choose a photo of the happy couple, the proud parents, or anything else you wish</li>
    <li><svg width="20" height="26" style="color:#fff"><use href="#drop"/></svg>Choose any size or shape you wish, up to 24x36"</li>
    <li><svg width="20" height="26" style="color:#fff"><use href="#drop"/></svg>We take care of all production and customization</li>
  </ul>
  <span class="btn">Check price and availability</span>
</section>

<!-- section 3 -->
<section class="abs" style="left:152px;top:2310px;width:440px">
  <h2 class="heading">Choose one of our standard spouts, or <em>design your own</em></h2>
  <ul class="points" style="margin-top:30px">
    <li><svg width="20" height="26" style="color:var(--blue)"><use href="#drop"/></svg>Choose one of our standard spouts – wedding cake, flower vase, or "just married" car. More spout decorations will be added each month</li>
    <li><svg width="20" height="26" style="color:var(--blue)"><use href="#drop"/></svg>For an additional fee, our team of 3D designers will design, 3D print, and decorate a spout just for your event</li>
  </ul>
  <span class="btn">Check price and availability</span>
</section>
<svg class="abs" style="left:630px;top:2230px" width="360" height="660" viewBox="0 0 360 660" role="img" aria-label="Sanitizer tower with a wedding cake spout decoration">
  <ellipse cx="180" cy="330" rx="170" ry="320" fill="#c9c4b6"/><ellipse cx="180" cy="330" rx="170" ry="320" fill="none" stroke="#1b9bd7" stroke-width="6"/>
</svg>

<!-- section 4 -->
<svg class="abs" style="left:0;top:2920px" width="1200" height="840" viewBox="0 0 1200 840">
  <path d="M0 60 C400 -20 800 120 1200 20 L1200 780 C800 840 400 740 0 800Z" fill="url(#band)"/>
  <path d="M340 90 C300 250 100 380 100 560 a240 240 0 0 0 480 0 C580 380 380 250 340 90Z" fill="#b7b4ae" role="img" aria-label="Sleek sanitizer tower in a hallway"/>
</svg>
<section class="abs on-blue" style="left:628px;top:3130px;width:470px">
  <h2 class="heading">Greet your guests with an act of care</h2>
  <ul class="points" style="margin-top:30px">
    <li><svg width="20" height="26" style="color:#fff"><use href="#drop"/></svg>Make your friends and family feel welcome and safe with a rugged, durable hand sanitizer from Purvant</li>
    <li><svg width="20" height="26" style="color:#fff"><use href="#drop"/></svg>Our battery-powered dispensers are reliable, wireless, and touchless</li>
    <li><svg width="20" height="26" style="color:#fff"><use href="#drop"/></svg>Filled with your choice from our wide range of sanitizing products</li>
  </ul>
  <span class="btn">Check price and availability</span>
</section>

<!-- section 5 -->
<section class="abs" style="left:152px;top:3830px;width:480px">
  <h2 class="heading">Sanitizing as a service means <em>low upfront investment</em></h2>
  <ul class="points" style="margin-top:30px">
    <li><svg width="20" height="26" style="color:var(--blue)"><use href="#drop"/></svg>Purchase our tower outright, or lease it for a low monthly rate on a two-year plan</li>
    <li><svg width="20" height="26" style="color:var(--blue)"><use href="#drop"/></svg>Monthly lease plan includes sanitizing fluid, online reporting, one year warranty, and tower rental</li>
    <li><svg width="20" height="26" style="color:var(--blue)"><use href="#drop"/></svg>Prices start at $3 per day – less than a cup of coffee! Volume discounts available</li>
  </ul>
  <span class="btn">Check price and availability</span>
</section>
<svg class="abs" style="left:720px;top:3770px" width="370" height="680" viewBox="0 0 370 680" role="img" aria-label="Wedding photo sanitizer tower with cake spout">
  <path d="M10 40 L360 0 L360 680 L10 680Z" fill="#cfc2bb"/>
</svg>

<!-- footer -->
<svg class="abs" style="left:0;top:4420px" width="1200" height="316" viewBox="0 0 1200 316">
  <path d="M0 40 C400 0 800 80 1200 20 L1200 316 L0 316Z" fill="var(--foot)"/>
  <path d="M0 40 C400 0 800 80 1200 20" fill="none" stroke="#1b9bd7" stroke-width="6"/>
</svg>
<div class="abs social"><span></span><span></span><span></span></div>
<p class="abs footer-text" style="top:4608px">© COPYRIGHT 2021 PURVANT LLC • SITEMAP • PRIVACY POLICY</p>
<div class="abs foot-brand">purvant</div>
</body>
</html>
```